Birch Flooring Supply

Basic one-sided business card design using the attached logo. Vintage americana theme. Font is modified Arial Nova Cond, but anything that coordinates can be used

```html
<!DOCTYPE html>
<html lang="en">
<head>
<meta charset="utf-8">
<title>Birch Flooring Supply – Business Card</title>
<link href="https://fonts.googleapis.com/css2?family=Oswald:wght@400;600&display=swap" rel="stylesheet">
<style>
  :root {
    --stage: #2b2b2b;
    --card-black: #1c1c1c;
    --kraft: #b3976f;
    --ink: #161616;
    --tan: #b3976f;
    --cream: #f2ede4;
  }
  * { box-sizing: border-box; margin: 0; padding: 0; }
  html, body {
    width: 1200px; height: 689px; overflow: hidden;
    background: var(--stage);
    font-family: "Oswald", "Arial Narrow", sans-serif;
  }
  .stage { position: relative; width: 1200px; height: 689px; }
  .card {
    position: absolute; top: 196px;
    width: 520px; height: 297px;
    border-radius: 16px; overflow: hidden;
  }
  .card--front { left: 45px; background: var(--card-black); }
  .card--back { left: 635px; background: var(--kraft); }

  .brand {
    position: absolute; display: flex; flex-direction: column;
    align-items: center; justify-content: center; text-align: center;
  }
  .brand__ring {
    position: absolute; inset: 0; border-radius: 50%;
    border: 3px solid var(--tan);
  }
  .brand__name {
    position: relative; color: var(--cream);
    font-weight: 600; text-transform: uppercase;
    letter-spacing: 1px; line-height: 1.05;
  }
  .card--front .brand { width: 180px; height: 180px; left: 170px; top: 58px; }
  .card--front .brand__name { font-size: 27px; }

  .back__disc {
    position: absolute; width: 300px; height: 300px;
    right: -40px; top: -70px; border-radius: 50%;
    background: var(--card-black);
  }
  .card--back .brand { width: 165px; height: 165px; right: 26px; top: 0px; }
  .card--back .brand__name { font-size: 24px; }

  .contact { position: absolute; left: 36px; top: 76px; color: var(--ink); }
  .contact__name {
    font-weight: 600; font-size: 26px; letter-spacing: 1px;
    text-transform: uppercase; line-height: 1;
  }
  .contact__title { font-weight: 600; font-size: 15px; line-height: 20px; margin-top: 4px; }
  .contact__list { list-style: none; margin-top: 8px; margin-left: 14px; }
  .contact__item {
    display: flex; align-items: flex-start; gap: 10px;
    font-size: 12.5px; line-height: 16px; margin-bottom: 2px;
  }
  .contact__icon { width: 12px; height: 12px; margin-top: 2px; flex: none; fill: var(--ink); }
</style>
</head>
<body>
<main class="stage">
  <section class="card card--front" aria-label="Card front">
    <div class="brand">
      <span class="brand__ring"></span>
      <span class="brand__name">Birch<br>Flooring<br>Supply</span>
    </div>
  </section>

  <section class="card card--back" aria-label="Card back">
    <div class="back__disc"></div>
    <div class="brand">
      <span class="brand__ring"></span>
      <span class="brand__name">Birch<br>Flooring<br>Supply</span>
    </div>

    <div class="contact">
      <h1 class="contact__name">Daniel Reyes</h1>
      <p class="contact__title">Founder&amp; CEO</p>
      <ul class="contact__list">
        <li class="contact__item">
          <svg class="contact__icon" viewBox="0 0 12 12"><path d="M6 0a4 4 0 0 0-4 4c0 3 4 8 4 8s4-5 4-8a4 4 0 0 0-4-4zm0 5.5A1.5 1.5 0 1 1 6 2.5a1.5 1.5 0 0 1 0 3z"/></svg>
          <span>4471 Alder Lane<br>Milford, CT 06460</span>
        </li>
        <li class="contact__item">
          <svg class="contact__icon" viewBox="0 0 12 12"><path d="M2.5 0.5l2 2.5-1.2 1.5a7 7 0 0 0 4.2 4.2L9 7.5l2.5 2-1.5 2C5 11 1 7 0.5 2z"/></svg>
          <span>555-201-4417</span>
        </li>
        <li class="contact__item">
          <svg class="contact__icon" viewBox="0 0 12 12"><path d="M3 0h6v12H3zM4 1.5v8h4v-8z"/></svg>
          <span>555-208-3392</span>
        </li>
        <li class="contact__item">
          <svg class="contact__icon" viewBox="0 0 12 12"><path d="M3 0h6v3H3zM1 4h10v5H9v3H3V9H1zm3 4v3h4V8z"/></svg>
          <span>555-214-7760</span>
        </li>
        <li class="contact__item">
          <svg class="contact__icon" viewBox="0 0 12 12"><path d="M0 2h12v8H0zm1 1l5 4 5-4z"/></svg>
          <span>info@birchflooringsupply.com</span>
        </li>
        <li class="contact__item">
          <svg class="contact__icon" viewBox="0 0 12 12"><path d="M6 0a6 6 0 1 0 0 12A6 6 0 0 0 6 0zm0 1.2c.8.9 1.3 2.6 1.4 4.2H4.6C4.7 3.8 5.2 2.1 6 1.2zM1.3 6.6h2.2c.1 1.5.5 2.9 1.1 3.9a4.8 4.8 0 0 1-3.3-3.9zm3.3 0h2.8c-.1 1.6-.6 3.2-1.4 4.2-.8-1-1.3-2.6-1.4-4.2zm2.8 3.9c.6-1 1-2.4 1.1-3.9h2.2a4.8 4.8 0 0 1-3.3 3.9z"/></svg>
          <span>birchflooringsupply.com</span>
        </li>
      </ul>
    </div>
  </section>
</main>
</body>
</html>
```